sommelier *

Sommelier Wine Hospitality Tavergne Crest experience I'm working as a sommelier in a Tavergne Crest restaurant. I try to reach People who are interested in invest in wine and wine loovers! In terms of color I would like to have a nice color based on a nice bordeaux red (as an advice). By the way i forgot to write my phone number and my email address. 438271905316 kdorvan4@quillpost.net I hope this info is enough so far.

```html
<!DOCTYPE html>
<html lang="en">
<head>
<meta charset="utf-8">
<title>Julian Varek – Sommelier Business Card</title>
<link rel="stylesheet" href="https://fonts.googleapis.com/css2?family=Caveat:wght@600&family=Ubuntu:wght@400&display=swap">
<style>
  :root {
    --backdrop: #1f1f21;
    --gold-card: #e9b252;
    --bordeaux: #5a0620;
    --bordeaux-deep: #3f0316;
    --gold-ink: #e8a83e;
    --faint-glass: rgba(255, 255, 255, 0.10);
  }
  * { box-sizing: border-box; margin: 0; padding: 0; }
  html, body {
    width: 1200px;
    height: 800px;
    overflow: hidden;
    background: var(--backdrop);
  }
  .canvas {
    position: relative;
    width: 1200px;
    height: 800px;
  }
  .card {
    position: absolute;
    left: 330px;
    width: 540px;
    height: 308px;
    border-radius: 2px;
    box-shadow: 0 18px 40px rgba(0, 0, 0, 0.55);
    overflow: hidden;
  }
  .card--front {
    top: 60px;
    background: var(--gold-card);
  }
  .card--back {
    top: 432px;
    background: var(--bordeaux);
  }
  .front-emblem {
    position: absolute;
    left: 246px;
    top: 96px;
    width: 48px;
    height: 96px;
    border-radius: 24px 24px 6px 6px;
    background: var(--bordeaux);
  }
  .back-decoration {
    position: absolute;
    right: -40px;
    top: 18px;
    width: 170px;
    height: 300px;
    border-radius: 80px 80px 20px 20px;
    background: var(--faint-glass);
  }
  .holder {
    position: absolute;
    left: 70px;
    top: 62px;
  }
  .holder__name {
    font-family: "Caveat", cursive;
    font-weight: 600;
    font-size: 40px;
    line-height: 1;
    color: var(--gold-ink);
  }
  .holder__role {
    margin-top: 8px;
    font-family: "Ubuntu", sans-serif;
    font-size: 14px;
    color: var(--gold-ink);
  }
  .contacts {
    position: absolute;
    left: 70px;
    top: 218px;
    list-style: none;
  }
  .contacts__item {
    display: flex;
    align-items: center;
    gap: 16px;
    font-family: "Ubuntu", sans-serif;
    font-size: 15px;
    color: var(--gold-ink);
    margin-bottom: 12px;
  }
  .contacts__icon {
    width: 18px;
    height: 18px;
    flex: none;
  }
</style>
</head>
<body>
  <main class="canvas">
    <section class="card card--front" aria-label="Card front">
      <div class="front-emblem" role="img" aria-label="Outline wine glass emblem with bordeaux wine"></div>
    </section>

    <section class="card card--back" aria-label="Card back">
      <div class="back-decoration" role="img" aria-label="Large faint wine glass decoration"></div>

      <div class="holder">
        <h1 class="holder__name">Julian Varek</h1>
        <p class="holder__role">Sommelier</p>
      </div>

      <ul class="contacts">
        <li class="contacts__item">
          <svg class="contacts__icon" viewBox="0 0 24 24" aria-hidden="true">
            <path fill="#e8a83e" d="M6.6 10.8a15.1 15.1 0 0 0 6.6 6.6l2.2-2.2c.3-.3.7-.4 1-.2 1.1.4 2.3.6 3.6.6.6 0 1 .4 1 1V20c0 .6-.4 1-1 1A17 17 0 0 1 3 4c0-.6.4-1 1-1h3.5c.6 0 1 .4 1 1 0 1.3.2 2.5.6 3.6.1.3 0 .7-.2 1z"/>
          </svg>
          <span>+49 438271905316</span>
        </li>
        <li class="contacts__item">
          <svg class="contacts__icon" viewBox="0 0 24 24" aria-hidden="true">
            <rect x="2" y="5" width="20" height="14" rx="1" fill="#e8a83e"/>
            <polyline points="2,6 12,13 22,6" fill="none" stroke="#5a0620" stroke-width="1.6"/>
          </svg>
          <span>kdorvan4@quillpost.net</span>
        </li>
      </ul>
    </section>
  </main>
</body>
</html>
```